Design a Facebook Cover Photo for Graphic Designer

We need a kick ass new Facebook cover for our graphic design studio. We want it to be mobile friendly so it displays properly on a smart phone as well. (It's currently being cut off see screenshot below of what we are currently using). Essentially, we want something really edgy, to communicate our personality and inform people what we do. We would also like the jpeg, png and psd files.

The main services we provide are:
- Graphic Design
- Web Design

What you need to know:
This is currently what we use. [login to view URL]

Fonts in our logo are:
Ostrich Sans
Grand Hotel

Any other questions please let us know.

```html
<!DOCTYPE html>
<html lang="en">
<head>
<meta charset="utf-8">
<title>Foldline Studio – Cover</title>
<link rel="stylesheet" href="https://fonts.googleapis.com/css2?family=Lustria&family=Grand+Hotel&family=Montserrat:wght@600;800&family=Open+Sans:wght@300;400&display=swap">
<style>
  :root {
    --navy: #1d3f73;
    --deep-blue: #2a5d93;
    --mid-blue: #4b7fc5;
    --bright-blue: #3c6fc4;
    --teal: #3a8fb0;
    --ice: #d8eef3;
    --white: #ffffff;
    --logo-teal: #4aa6c4;
    --band: rgba(22, 52, 96, 0.88);
  }
  * { margin: 0; padding: 0; box-sizing: border-box; }
  html, body { width: 1200px; height: 444px; overflow: hidden; background: var(--white); }
  .cover {
    position: relative;
    width: 1200px;
    height: 444px;
    overflow: hidden;
  }
  .cover__backdrop {
    position: absolute;
    inset: 0;
    background:
      linear-gradient(115deg, rgba(255,255,255,0.55) 0%, rgba(255,255,255,0) 14%),
      linear-gradient(100deg, var(--deep-blue) 0%, var(--teal) 32%, #5aa9c7 55%, #9fcfe0 78%, var(--ice) 100%);
  }
  .service-tags {
    position: absolute;
    inset: 0;
    width: 1200px;
    height: 444px;
  }
  .service-tag__label {
    font-family: "Lustria", serif;
    font-size: 38px;
    fill: var(--white);
    text-anchor: middle;
  }
  .tagline {
    position: absolute;
    left: 338px;
    top: 222px;
    display: flex;
    align-items: baseline;
    gap: 14px;
    color: var(--white);
    white-space: nowrap;
  }
  .tagline__script {
    font-family: "Grand Hotel", cursive;
    font-size: 54px;
  }
  .tagline__link {
    font-family: "Montserrat", sans-serif;
    font-weight: 600;
    font-size: 24px;
    letter-spacing: 1px;
  }
  .tagline__bold {
    font-family: "Montserrat", sans-serif;
    font-weight: 800;
    font-size: 40px;
    letter-spacing: 3px;
  }
  .brand-panel {
    position: absolute;
    left: 0;
    top: 240px;
    width: 261px;
    height: 204px;
    background: var(--white);
    display: flex;
    align-items: center;
    justify-content: center;
  }
  .brand-panel__name {
    font-family: "Lustria", serif;
    font-size: 34px;
    color: var(--logo-teal);
  }
  .contact-band {
    position: absolute;
    right: 0;
    bottom: 0;
    width: 650px;
    height: 70px;
  }
  .contact-band__shape { position: absolute; inset: 0; }
  .contact-band__text {
    position: absolute;
    right: 22px;
    top: 20px;
    font-family: "Open Sans", sans-serif;
    font-weight: 400;
    font-size: 22px;
    color: var(--white);
    white-space: nowrap;
  }
</style>
</head>
<body>
<main class="cover">
  <div class="cover__backdrop" role="img" aria-label="Faceted low-poly background in deep blue fading to pale cyan"></div>

  <svg class="service-tags" viewBox="0 0 1200 444" aria-label="Services">
    <g class="service-tag service-tag--brand">
      <polygon points="30,62 386,54 398,146 62,138" fill="var(--navy)" stroke="var(--white)" stroke-width="4" stroke-linejoin="round"/>
      <polygon points="44,70 374,64 384,136 70,130" fill="none" stroke="rgba(255,255,255,0.35)" stroke-width="2"/>
      <text class="service-tag__label" x="214" y="112">Brand Identity</text>
    </g>
    <g class="service-tag service-tag--print">
      <polygon points="498,28 760,40 770,132 488,122" fill="var(--mid-blue)" stroke="var(--white)" stroke-width="4" stroke-linejoin="round"/>
      <polygon points="508,38 750,48 758,124 500,114" fill="none" stroke="rgba(255,255,255,0.35)" stroke-width="2"/>
      <text class="service-tag__label" x="630" y="97">Print Design</text>
    </g>
    <g class="service-tag service-tag--web">
      <polygon points="868,40 1150,14 1178,146 880,132" fill="var(--bright-blue)" stroke="var(--white)" stroke-width="4" stroke-linejoin="round"/>
      <polygon points="880,48 1140,24 1164,136 890,124" fill="none" stroke="rgba(255,255,255,0.35)" stroke-width="2"/>
      <text class="service-tag__label" x="1022" y="100">Web Design</text>
    </g>
  </svg>

  <h1 class="tagline">
    <span class="tagline__script">Small Studio</span>
    <span class="tagline__link">WITH</span>
    <span class="tagline__bold">BIG PERSONALITY</span>
  </h1>

  <div class="brand-panel">
    <span class="brand-panel__name">foldline studio</span>
  </div>

  <div class="contact-band">
    <svg class="contact-band__shape" viewBox="0 0 650 70" preserveAspectRatio="none" aria-hidden="true">
      <polygon points="30,0 650,0 650,70 0,70" fill="var(--band)"/>
    </svg>
    <p class="contact-band__text">creative@foldlinestudio.com.au | 040 555 0187</p>
  </div>
</main>
</body>
</html>
```